Recruitment #1

We are looking for an effective ad to recruit work from home Loan Officers for our Mortgage Brokerage.
Use the following text...
Earn Mortgage Income in your sleep. Its as easy as 1, 2, 3.....
1) Solicit Potential Applicants (Word of Mouth, Email, Social Media etc.)
2) Take Complete Applications & Submit Them
3) Wait to Get Paid.......(Avg. $2,500 per closing)
"You open the Bluegate, We'll handle the rest"
No Experience Necessary
No Goals or Quotas
No Office Hours / Work from Home Office
...and We Fully Reimburse ALL LICENSING FEES!!
Email Resume to mkowal@bluegatehomeloans.com
Bluegate Financial Services, Inc.
731 W Orchard Avenue, #318
Baltimore, MD 21417
NMLS #386147
www.bluegatehomeloans.com
Phone (800) 640-2915
Licensed Mortgage Broker in MD and DC since 1997
Professionals looking to earn part time income at Loan Officers, preferably with strong social media following.
Loan

```html
<!DOCTYPE html>
<html lang="en">
<head>
<meta charset="utf-8">
<title>Bluegate Financial Services – Loan Officer Recruitment</title>
<link href="https://fonts.googleapis.com/css2?family=Archivo+Black&family=Arimo:ital,wght@0,400;0,700;1,700&family=Tinos:wght@700&display=swap" rel="stylesheet">
<style>
  :root {
    --brand-blue: #1a5ea8;
    --deep-blue: #0f4f9e;
    --gold: #b39a30;
    --gray: #6d6e70;
    --ink: #111;
    --white: #fff;
  }
  html, body { margin: 0; padding: 0; overflow: hidden; }
  body { width: 927px; height: 1200px; background: var(--white); }
  .flyer { position: relative; width: 927px; height: 1200px; overflow: hidden; background: var(--white); font-family: "Arimo", Arial, sans-serif; }
  .backdrop { position: absolute; inset: 0; }
  .abs { position: absolute; margin: 0; }

  .brand { left: 64px; top: 150px; display: flex; align-items: center; gap: 12px; }
  .brand-dot { width: 34px; height: 34px; border-radius: 50%; background: var(--brand-blue); }
  .brand-name { font-family: "Tinos", serif; font-weight: 700; font-size: 27px; color: var(--brand-blue); }

  .headline { left: 56px; top: 292px; font-family: "Archivo Black", sans-serif; font-size: 51px; line-height: 45px; color: var(--brand-blue); text-transform: uppercase; }
  .subhead { left: 56px; top: 478px; font-family: "Archivo Black", sans-serif; font-size: 38px; line-height: 45px; color: var(--gray); }

  .steps { left: 56px; top: 582px; list-style: none; padding: 0; }
  .step { display: flex; gap: 9px; font-size: 19px; line-height: 21px; color: var(--ink); }
  .step + .step { margin-top: 20px; }
  .step-num { flex: none; width: 40px; height: 40px; border-radius: 50%; background: var(--gold); color: var(--white); font-family: "Archivo Black", sans-serif; font-size: 24px; display: flex; align-items: center; justify-content: center; margin-top: 2px; }
  .step-num::after { content: ""; }

  .contact { left: 56px; top: 890px; font-family: "Tinos", serif; font-weight: 700; font-size: 16px; line-height: 18px; color: var(--ink); }
  .contact-row { display: flex; gap: 10px; align-items: flex-start; margin-top: 9px; }
  .contact-row svg { flex: none; width: 24px; height: 24px; margin-top: -2px; }
  .company { padding-left: 32px; }

  .social { left: 58px; top: 1038px; width: 188px; height: 60px; border: 2px solid var(--brand-blue); display: flex; align-items: center; gap: 10px; padding: 0 10px; box-sizing: border-box; }
  .social-square { width: 32px; height: 32px; background: var(--brand-blue); flex: none; }
  .social-name { font-size: 16px; font-weight: 700; color: var(--brand-blue); line-height: 18px; }

  .licence { left: 56px; top: 1113px; font-size: 17.5px; font-weight: 700; line-height: 18px; color: var(--ink); }

  .quote-text { left: 470px; top: 664px; width: 372px; text-align: center; font-family: "Archivo Black", sans-serif; font-size: 37px; line-height: 35px; color: var(--white); text-transform: uppercase; }
  .perks { left: 420px; top: 876px; width: 474px; text-align: center; font-style: italic; font-weight: 700; font-size: 21px; line-height: 27px; color: var(--white); }
  .reimburse { left: 420px; top: 978px; width: 474px; text-align: center; color: var(--white); font-weight: 700; }
  .reimburse-lead { display: block; font-style: italic; font-size: 27px; line-height: 30px; }
  .reimburse-main { display: block; font-family: "Archivo Black", sans-serif; font-size: 30px; line-height: 32px; }
  .apply { left: 420px; top: 1092px; width: 474px; text-align: center; font-family: "Tinos", serif; font-weight: 700; font-size: 26px; line-height: 29px; color: var(--gold); }
</style>
</head>
<body>
<main class="flyer">
  <svg class="backdrop" width="927" height="1200" viewBox="0 0 927 1200" aria-hidden="true">
    <defs>
      <linearGradient id="panel" x1="0" y1="0" x2="0" y2="1">
        <stop offset="0" stop-color="#1d4fa0"/>
        <stop offset="0.45" stop-color="#1a5ea8"/>
        <stop offset="1" stop-color="#1a5ea8"/>
      </linearGradient>
    </defs>
    <path d="M432 0 C 520 120, 500 330, 470 470 C 450 560, 428 600, 424 640 C 420 760, 420 900, 428 1000 C 436 1090, 444 1150, 450 1200 L 927 1200 L 927 0 Z" fill="var(--gold)"/>
    <path d="M432 0 C 520 120, 500 330, 470 470 C 460 560, 440 600, 434 640 C 430 760, 430 900, 438 1000 C 446 1090, 454 1150, 462 1200 L 927 1200 L 927 0 Z" fill="url(#panel)"/>
  </svg>

  <svg class="abs" style="left:446px;top:0" width="481" height="620" viewBox="0 0 481 620" role="img" aria-label="Tinted photograph of a modern glass office tower">
    <defs>
      <linearGradient id="tower" x1="0" y1="0" x2="1" y2="1">
        <stop offset="0" stop-color="#2a4d9a" stop-opacity="0.9"/>
        <stop offset="1" stop-color="#3d7cc4" stop-opacity="0.4"/>
      </linearGradient>
    </defs>
    <path d="M30 0 H481 V620 H0 C 40 420, 60 160, 30 0 Z" fill="url(#tower)"/>
  </svg>

  <svg class="abs" style="left:436px;top:316px" width="384" height="308" viewBox="0 0 384 308" role="img" aria-label="Photograph of a smiling young woman holding a fan of dollar bills">
    <defs>
      <radialGradient id="portrait" cx="0.45" cy="0.45" r="0.6">
        <stop offset="0" stop-color="#d9c2b3"/>
        <stop offset="0.6" stop-color="#8f7e76"/>
        <stop offset="1" stop-color="#4f5258" stop-opacity="0"/>
      </radialGradient>
    </defs>
    <rect width="384" height="308" fill="url(#portrait)"/>
  </svg>

  <svg class="abs" style="left:420px;top:620px" width="480" height="240" viewBox="0 0 480 240" aria-hidden="true">
    <path d="M30 4 H442 V64 M442 148 V234 H30 V90" fill="none" stroke="var(--gold)" stroke-width="4"/>
    <text x="-2" y="86" font-family="Archivo Black, sans-serif" font-size="110" fill="var(--gold)">“</text>
    <text x="406" y="198" font-family="Archivo Black, sans-serif" font-size="110" fill="var(--gold)">”</text>
  </svg>

  <div class="abs brand">
    <span class="brand-dot"></span>
    <span class="brand-name">Bluegate Financial Services, Inc.</span>
  </div>

  <h1 class="abs headline">Earn<br>Mortgage<br>Income in<br>Your Sleep.</h1>
  <p class="abs subhead">IT’S AS EASY AS<br>1, 2, 3...</p>

  <ol class="abs steps">
    <li class="step"><span class="step-num">1</span><span>Solicit Potential Applicants<br>(Word of Mouth, Email,<br>Social Media etc.)</span></li>
    <li class="step" style="margin-top:24px"><span class="step-num">2</span><span>Take Complete Applications<br>&amp; Submit Them</span></li>
    <li class="step" style="margin-top:22px"><span class="step-num">3</span><span>Wait to Get Paid.......<br>(Avg. $2,500 per closing)</span></li>
  </ol>

  <address class="abs contact" style="font-style:normal">
    <div class="company">Bluegate Financial Services, Inc.</div>
    <div class="contact-row">
      <svg viewBox="0 0 24 24"><path d="M12 2a7 7 0 0 0-7 7c0 5 7 13 7 13s7-8 7-13a7 7 0 0 0-7-7zm0 9.5A2.5 2.5 0 1 1 12 6.5a2.5 2.5 0 0 1 0 5z" fill="var(--brand-blue)"/></svg>
      <span>731 W Orchard Avenue, #318<br>Baltimore, MD 21417<br>NMLS #386147</span>
    </div>
    <div class="contact-row">
      <svg viewBox="0 0 24 24" fill="none" stroke="var(--brand-blue)" stroke-width="1.6"><circle cx="12" cy="12" r="10"/><ellipse cx="12" cy="12" rx="4.5" ry="10"/><path d="M2 12h20M4 6.5h16M4 17.5h16"/></svg>
      <span>www.bluegatehomeloans.com</span>
    </div>
    <div class="contact-row">
      <svg viewBox="0 0 24 24"><circle cx="12" cy="12" r="11" fill="var(--brand-blue)"/><path d="M8.5 6.5l2 2.2-1.2 1.6c.8 1.7 2.1 3 3.8 3.8l1.6-1.2 2.2 2-1.2 1.9c-3.8-.3-7.6-4.1-7.9-7.9z" fill="var(--white)"/></svg>
      <span>Phone (800) 640-2915</span>
    </div>
  </address>

  <div class="abs social">
    <span class="social-square"></span>
    <span class="social-name">Like us on<br>Friendbook</span>
  </div>

  <p class="abs licence">Licensed Mortgage Broker<br>in MD and DC since 1997</p>

  <p class="abs quote-text">You open the<br>Bluegate,<br>We’ll handle<br>the rest.</p>

  <p class="abs perks">No Experience Necessary<br>No Goals or Quotas<br>No Office Hours / Work from Home Office</p>

  <p class="abs reimburse"><span class="reimburse-lead">...and We Fully Reimburse</span><span class="reimburse-main">ALL LICENSING FEES!!</span></p>

  <p class="abs apply">Email Resume to<br>mkowal@bluegatehomeloans.com</p>
</main>
</body>
</html>
```